Merrow Consulting needs a business card design

Merrow Consulting is a small business that consults and trains Australia wide in Workplace Health and Safety, Environment and Quality Management Systems.

Clients are typically smaller businesses with 50 to 200 employees but there are some large clients.

Communication is often by email, although mobile is used as well.

Merrow Consulting
41 Tulwin Ferris Road
Kingsholme, QLD 4208
0438 291 064

```html
<!DOCTYPE html>
<html lang="en">
<head>
<meta charset="utf-8">
<title>Merrow Consulting – Business Card</title>
<link href="https://fonts.googleapis.com/css2?family=Michroma&display=swap" rel="stylesheet">
<style>
  :root {
    --backdrop: #d9d9d9;
    --card: #fbfbfb;
    --card-front: #ececec;
    --front-panel: #dcdcdc;
    --ink-grey: #77787b;
    --ink-navy: #1b2750;
    --accent-blue: #1ea6e3;
    --rule: #9a9a9a;
  }
  * { margin: 0; padding: 0; box-sizing: border-box; }
  html, body {
    width: 1200px; height: 1200px; overflow: hidden;
    background: var(--backdrop);
    font-family: "Michroma", "Arial", sans-serif;
  }
  .stage {
    width: 1200px; height: 1200px;
    display: flex; align-items: center; justify-content: center; gap: 60px;
  }
  .card { box-shadow: 0 6px 18px rgba(0,0,0,0.12); position: relative; }

  /* Front */
  .card-front {
    width: 340px; height: 580px;
    background: var(--card-front);
    display: flex; align-items: center; justify-content: center;
  }
  .front-panel {
    width: 280px; height: 440px;
    background: var(--front-panel);
    border-radius: 34px;
    display: flex; align-items: center; justify-content: center;
  }
  .front-name {
    background: var(--card);
    padding: 26px 20px;
    display: flex; flex-direction: column; align-items: center; gap: 14px;
  }
  .brand-square { width: 40px; height: 40px; background: var(--accent-blue); }
  .front-name .brand-name {
    color: var(--ink-navy); font-size: 17px; line-height: 1.25; text-align: center; text-transform: uppercase;
  }

  /* Back */
  .card-back {
    width: 600px; height: 340px;
    background: var(--card);
    color: var(--ink-grey);
    text-transform: uppercase;
  }
  .back-brand {
    position: absolute; left: 44px; top: 48px;
    display: flex; align-items: center; gap: 16px;
  }
  .back-brand .brand-square { width: 30px; height: 30px; }
  .back-brand .divider { width: 1px; height: 60px; background: var(--rule); }
  .back-brand .brand-name { color: var(--ink-grey); font-size: 17px; line-height: 1.2; }
  .side-rule {
    position: absolute; right: 36px; top: 40px; bottom: 40px;
    width: 1px; background: var(--rule);
  }
  .address {
    position: absolute; left: 44px; bottom: 42px;
    font-size: 9.5px; line-height: 1.9; letter-spacing: 0.3px;
    font-style: normal; white-space: nowrap;
  }
  .address .company {
    padding-bottom: 6px; margin-bottom: 6px;
    border-bottom: 1px solid var(--rule);
  }
  .contact {
    position: absolute; right: 56px; bottom: 60px;
    font-size: 9.5px; line-height: 1.9; letter-spacing: 0.3px;
    white-space: nowrap;
  }
  .contact .label { color: var(--accent-blue); margin-right: 6px; }
</style>
</head>
<body>
  <main class="stage">
    <section class="card card-front" aria-label="Business card front">
      <div class="front-panel">
        <div class="front-name">
          <span class="brand-square"></span>
          <span class="brand-name">Merrow<br>Consulting</span>
        </div>
      </div>
    </section>

    <section class="card card-back" aria-label="Business card back">
      <div class="back-brand">
        <span class="brand-square"></span>
        <span class="divider"></span>
        <span class="brand-name">Merrow<br>Consulting</span>
      </div>
      <div class="side-rule"></div>
      <address class="address">
        <div class="company">Merrow Consulting</div>
        <div>41 Tulwin Ferris Road</div>
        <div>Kingsholme, QLD 4208</div>
      </address>
      <div class="contact">
        <div><span class="label">P:</span>0438 291 064</div>
        <div><span class="label">E:</span>info@merrowconsulting.com</div>
      </div>
    </section>
  </main>
</body>
</html>
```